Vorn Solutions: searching for a flyer to trow in letterboxes for properties we are interested in

Hello ,

Introduction:
We are a company based in Luxembourg called "Vorn Solutions". We are specialized in buying properties on which we develop and build constructions before selling them.

Informations for the flyer:
We need a flyer to trow into the letter boxes of property owners letting them know that we are interested in buying their property, if they are interested they can give us a call.

The text for the flyer/letter is in the attachment called >>2020-03-11_VS_Text for flyer,letter there might be slight changes<<.

We need to look competent, professional and financially stable.

The flyer needs to be short and not over welling with information otherwise it will land in the trash.

We have decided that we don't want real pictures on the flyer, but shapes of any kind, blue prints, drawings are fine.

Format should be in DIN A4. We plan to print the flyer on both sides in two different languages, in other words the design will be the same on both sides only the text will be in a different language.

I also added our current logo and here is the design of the website that is under construction at the moment http://www.vornsolutions.example/. The logo's color can be changed into a different blue or uni color (all white or all black).
Updates

Hi, First time user the howl thing started faster as expected. Furthermore, I need to catch my boss to discust the project with him and he is on a lot of meetings. Please give us a little bit more time. Thanks

Target Market(s)

Property owners

Requirements
Must have
• email, phone number, tax number (RCS), Tax number , matriculation and address.
see word file in attachment for information
Nice to have
• Our company logo, in one form or an other, you can be creative, the logo is in the attachment.
Should not have
• Real pictures

```html
<!DOCTYPE html>
<html lang="en">
<head>
<meta charset="utf-8">
<title>Vorn Solutions – Flyer</title>
<link href="https://fonts.googleapis.com/css2?family=Bebas+Neue&family=Source+Sans+3:wght@400;600&display=swap" rel="stylesheet">
<style>
  :root {
    --stage: #e6e7e9;
    --paper: #ffffff;
    --blue-deep: #1b5f93;
    --blue-mid: #2d7fba;
    --blue-sky: #29a3dc;
    --mist: #eef0f2;
    --ink: #444444;
    --ink-dark: #1d2f45;
    --bar: #333335;
  }
  * { box-sizing: border-box; margin: 0; padding: 0; }
  html, body { width: 935px; height: 1200px; overflow: hidden; }
  body { background: var(--stage); font-family: "Source Sans 3", Arial, sans-serif; }

  .flyer {
    position: absolute; left: 64px; top: 31px;
    width: 806px; height: 1137px;
    background: var(--paper);
    overflow: hidden;
  }
  .flyer-shapes { position: absolute; inset: 0; width: 806px; height: 1137px; }

  .headline {
    position: absolute; right: 32px; top: 42px;
    font-family: "Bebas Neue", Impact, sans-serif; font-weight: 400;
    font-size: 47px; line-height: 1; color: #fff; letter-spacing: .5px;
    white-space: nowrap;
  }
  .headline-rule {
    position: absolute; left: 595px; top: 111px; width: 179px; height: 2px; background: #fff;
  }
  .intro {
    position: absolute; right: 32px; top: 128px; width: 362px;
    text-align: right; color: #fff; font-size: 14.5px; line-height: 19px;
  }
  .intro p + p { margin-top: 19px; }

  .services-title {
    position: absolute; left: 36px; top: 436px;
    font-family: "Bebas Neue", Impact, sans-serif; font-weight: 400;
    font-size: 31px; line-height: 1; color: var(--ink-dark); white-space: nowrap;
  }
  .services-rule {
    position: absolute; left: 36px; top: 485px; width: 175px; height: 2px; background: var(--blue-mid);
  }
  .service-list { position: absolute; left: 33px; top: 503px; list-style: none; }
  .service-list li {
    display: flex; align-items: center; height: 45px;
    font-size: 21px; color: var(--ink); white-space: nowrap;
  }
  .service-list svg { width: 50px; height: 34px; margin-right: 15px; }
  .services-text {
    position: absolute; left: 31px; top: 650px; width: 430px;
    font-size: 15.5px; line-height: 18.5px; color: var(--ink); text-align: justify;
  }

  .quote-badge {
    position: absolute; left: 512px; top: 505px; width: 130px; height: 130px;
    border-radius: 50%; background: var(--blue-sky); border: 4px solid #fff;
    box-shadow: 0 3px 8px rgba(0,0,0,.25);
    display: flex; align-items: center; justify-content: center; text-align: center;
    font-family: "Bebas Neue", Impact, sans-serif; font-size: 21px; line-height: 22px; color: #fff;
  }

  .brand-mark { position: absolute; left: 104px; top: 812px; width: 62px; height: 62px; background: var(--blue-deep); }
  .brand-name {
    position: absolute; left: 40px; top: 906px;
    font-family: "Source Sans 3", Arial, sans-serif; font-weight: 600;
    font-size: 28px; line-height: 1; color: var(--ink-dark); letter-spacing: .5px; white-space: nowrap;
  }
  .contact-list { position: absolute; left: 38px; top: 961px; list-style: none; }
  .contact-list li {
    display: flex; align-items: center; height: 26.6px;
    font-size: 16px; color: var(--ink); white-space: nowrap;
  }
  .contact-list svg { width: 18px; height: 18px; margin-right: 13px; }
</style>
</head>
<body>
<main class="flyer">
  <svg class="flyer-shapes" viewBox="0 0 597 842" preserveAspectRatio="none">
    <defs>
      <linearGradient id="blueBand" x1="0" y1="0" x2="1" y2="1">
        <stop offset="0" stop-color="#3a9bd6"/>
        <stop offset="1" stop-color="#1b5f93"/>
      </linearGradient>
      <linearGradient id="sketchTone" x1="0" y1="0" x2="1" y2="1">
        <stop offset="0" stop-color="#f6f6f6"/>
        <stop offset="1" stop-color="#d9dadc"/>
      </linearGradient>
      <linearGradient id="workbenchTone" x1="0" y1="0" x2="1" y2="1">
        <stop offset="0" stop-color="#d8b98c"/>
        <stop offset="1" stop-color="#b48a5a"/>
      </linearGradient>
    </defs>
    <rect x="0" y="0" width="597" height="279" fill="url(#blueBand)"/>
    <polygon points="0,0 173,0 252,279 0,279" fill="url(#sketchTone)" role="img" aria-label="Illustration of a detached house standing on architectural floor plans"/>
    <polygon points="173,279 252,150 252,279" fill="#9aa0a6" opacity=".6"/>

    <rect x="0" y="279" width="597" height="283" fill="var(--mist)" role="img" aria-label="Faint blueprint drawing background"/>
    <polygon points="285,200 380,200 597,560 597,600 500,600" fill="url(#blueBand)"/>
    <polygon points="380,279 597,279 597,590" fill="#2a78b2"/>
    <polygon points="0,281 272,281 370,455 262,560 0,560" fill="#ffffff" opacity=".92"/>

    <rect x="0" y="562" width="597" height="280" fill="#ffffff"/>
    <polygon points="285,562 560,562 597,600 597,842 335,842" fill="url(#workbenchTone)" role="img" aria-label="Photo of a small model house on building plans with a pencil and wood shavings"/>
    <polygon points="545,562 597,562 597,660" fill="var(--blue-deep)"/>
    <polygon points="372,781 394,842 318,842" fill="var(--blue-deep)"/>
    <rect x="0" y="817" width="316" height="25" fill="var(--bar)"/>
  </svg>

  <h1 class="headline">Are you thinking of seling?</h1>
  <div class="headline-rule"></div>
  <div class="intro">
    <p>Lorem ipsum dolor sit amet, consectetuer adipiscing elit, sed diam nonummy nibh euismod tincidunt ut laoreet dolore magna aliquam erat volutpat.</p>
    <p>Ut wisi enim ad minim veniam, quis nostrud exerci tation ullamcorper suscipit lobortis nisl ut aliquip ex ea commodo conse</p>
  </div>

  <h2 class="services-title">Constructions neuves et rénovations</h2>
  <div class="services-rule"></div>
  <ul class="service-list">
    <li><svg viewBox="0 0 50 34"><rect x="4" y="3" width="42" height="22" fill="none" stroke="#1b5f93" stroke-width="2"/><polyline points="10,19 16,11 22,16 28,8 34,14 40,9" fill="none" stroke="#1b5f93" stroke-width="2"/><line x1="14" y1="30" x2="36" y2="30" stroke="#1b5f93" stroke-width="2"/></svg>Promotion immobilière Achat-Vente</li>
    <li><svg viewBox="0 0 50 34"><rect x="4" y="4" width="42" height="26" fill="none" stroke="#1b5f93" stroke-width="2"/><rect x="10" y="9" width="30" height="16" fill="none" stroke="#1b5f93" stroke-width="1.5"/><circle cx="25" cy="17" r="5" fill="none" stroke="#1b5f93" stroke-width="1.5"/></svg>Gestion de travaux</li>
    <li><svg viewBox="0 0 50 34"><path d="M6 28 A19 19 0 0 1 44 28 Z" fill="none" stroke="#1b5f93" stroke-width="2"/><line x1="25" y1="10" x2="25" y2="28" stroke="#1b5f93" stroke-width="1.5"/><line x1="15" y1="14" x2="15" y2="28" stroke="#1b5f93" stroke-width="1.5"/><line x1="35" y1="14" x2="35" y2="28" stroke="#1b5f93" stroke-width="1.5"/></svg>Project manager</li>
  </ul>
  <p class="services-text">Lorem ipsum dolor sit amet, consectetuer adipiscing elit, sed diam nonummy nibh euismod tincidunt ut laoreet dolore magna aliquam erat volutpat. Ut wisi enim ad minim veniam, quis nostrud exerci tation ullamcorper suscipit lobortis nisl</p>

  <div class="quote-badge">Call us<br>for a<br>free quote</div>

  <div class="brand-mark"></div>
  <div class="brand-name">VORN SOLUTIONS</div>
  <ul class="contact-list">
    <li><svg viewBox="0 0 18 18"><rect width="18" height="18" rx="3" fill="#1b5f93"/><path d="M5 4 l2.5 0 1 3 -1.5 1 a7 7 0 0 0 3 3 l1 -1.5 3 1 0 2.5 a1 1 0 0 1 -1 1 A10 10 0 0 1 4 5 a1 1 0 0 1 1 -1z" fill="#fff"/></svg>+352 600.410.275 | 352 200.318.46</li>
    <li><svg viewBox="0 0 18 18"><rect width="18" height="18" rx="3" fill="#1b5f93"/><rect x="4" y="5.5" width="10" height="7" fill="none" stroke="#fff" stroke-width="1.3"/><polyline points="4,5.5 9,10 14,5.5" fill="none" stroke="#fff" stroke-width="1.3"/></svg>info@vornsolutions.example</li>
    <li><svg viewBox="0 0 18 18"><rect width="18" height="18" rx="3" fill="#1b5f93"/><path d="M9 15 C5 10 5 8.5 5 7.5 a4 4 0 0 1 8 0 c0 1 0 2.5 -4 7.5z" fill="#fff"/><circle cx="9" cy="7.5" r="1.5" fill="#1b5f93"/></svg>18 rue du Chantier, L-4012 Altheim</li>
    <li><svg viewBox="0 0 18 18"><rect width="18" height="18" rx="9" fill="#1b5f93"/><circle cx="9" cy="9" r="5" fill="none" stroke="#fff" stroke-width="1.2"/><ellipse cx="9" cy="9" rx="2.2" ry="5" fill="none" stroke="#fff" stroke-width="1"/><line x1="4" y1="9" x2="14" y2="9" stroke="#fff" stroke-width="1"/></svg>info@vornsolutions.example</li>
  </ul>
</main>
</body>
</html>
```